Logo + Label Design (Men’s Grooming Brand & Product Packaging)

Design a logo and 2 oz pomade label for Brant, a modern men’s grooming brand focused on clean, high-quality, natural ingredients. The design should establish a bold, masculine, minimalist identity that can later extend to products like shaving gel and body wash.

Key Requirements

Create a primary logo for “Brant” and a core label for the 2 oz pomade jar (screw-top).

Use a clean, modern style — masculine, confident, and approachable (think Wendel’s, Valto, Northfield Mill).

Design for 1–2 color screen printing on solid jar colors (white, black, or navy).

Avoid gradients, foil, or embossing. Must work in black & white.

Provide: vector logo, mockup of the 2 oz jar, color palette (CMYK/RGB/HEX), and font specs.

Winning design may lead to future projects (body wash, shave gel, skincare lines).

Font styles to use
Other font styles liked:
• We like the fonts and design concept in the attached mockup.

Requirements
Should not have
• We want to avoid too much writing or busy designs. We want to avoid having graphics/illustrations embedded in the logo if they will cause the brand to look less classy or sophisticated. We also want the design to look simple and all-American (e.g. Pellham and Stroud, Tall Pine, The BRIM, etc). We’d like to give a Kessler & Dunmore vibe that feels classy and high end.

```html
<!DOCTYPE html>
<html lang="en">
<head>
<meta charset="utf-8">
<title>Brant Hair Pomade – Lid and Label</title>
<link href="https://fonts.googleapis.com/css2?family=Roboto:wght@300;400;500;700;900&display=swap" rel="stylesheet">
<style>
  :root {
    --navy: #141c30;
    --stone: #d8d8d2;
    --paper: #ffffff;
    --ink-light: #e8e8e6;
    --rule-grey: #d4d4d4;
    --muted: #dadada;
    --font: "Roboto", Arial, sans-serif;
  }
  * { box-sizing: border-box; margin: 0; padding: 0; }
  html, body { width: 1200px; height: 599px; overflow: hidden; background: var(--paper); }
  body { position: relative; font-family: var(--font); color: var(--navy); }

  .section-title {
    position: absolute; top: 24px; font-size: 12px; font-weight: 500;
    text-decoration: underline; transform: translateX(-50%); color: #222;
  }
  .section-title--lid { left: 228px; }
  .section-title--label { left: 700px; }

  .lid { position: absolute; width: 240px; height: 240px; }
  .lid--navy { left: 106px; top: 55px; }
  .lid--white { left: 103px; top: 302px; }
  .lid text { font-family: var(--font); }

  .label {
    position: absolute; left: 396px; width: 680px; height: 170px;
    font-size: 7.6px; line-height: 10px;
  }
  .label--navy { top: 90px; background: var(--navy); color: var(--ink-light); }
  .label--white { top: 337px; background: var(--paper); color: var(--navy);
    box-shadow: 0 0 3px rgba(0,0,0,0.35); }

  .label__maker { position: absolute; left: 11px; top: 14px; }
  .label__bullets { position: absolute; left: 11px; top: 74px; list-style: none; }
  .label__heading { font-weight: 700; font-size: 7px; }

  .label__brand { position: absolute; left: 241px; top: 12px; width: 60px; text-align: center; }
  .brand-dot { width: 54px; height: 54px; border-radius: 50%; border: 7px solid currentColor; margin: 0 auto; }
  .brand-name { font-size: 22px; font-weight: 700; line-height: 30px; margin-top: 2px; letter-spacing: -0.3px; }

  .label__hold { position: absolute; left: 320px; top: 87px; font-size: 9.2px; font-weight: 500; }
  .label--white .label__hold { color: var(--muted); }
  .label__product { position: absolute; left: 241px; top: 109px; font-size: 16px; font-weight: 700; line-height: 20px; }
  .label__scent { position: absolute; left: 241px; top: 131px; font-size: 11px; font-weight: 300; line-height: 14px; }
  .label__weight { position: absolute; right: 240px; top: 133px; font-size: 9.5px; font-weight: 300; line-height: 12px; }

  .label__info { position: absolute; left: 460px; top: 14px; width: 210px; }
  .label__info p + .label__heading { margin-top: 6px; }
</style>
</head>
<body>
  <h2 class="section-title section-title--lid">Top Lid label</h2>
  <h2 class="section-title section-title--label">Label Design</h2>

  <svg class="lid lid--navy" viewBox="0 0 240 240" aria-label="Navy lid label">
    <defs>
      <path id="holdArcNavy" d="M 10,150 A 92 92 0 0 0 230,150"/>
    </defs>
    <circle cx="120" cy="120" r="113" fill="var(--navy)"/>
    <circle cx="120" cy="120" r="105" fill="none" stroke="var(--stone)" stroke-width="0.8"/>
    <text x="120" y="104" text-anchor="middle" font-size="48" font-weight="700" fill="var(--stone)" letter-spacing="-1">Brant</text>
    <rect x="37" y="144" width="80" height="22" fill="var(--stone)"/>
    <rect x="117" y="144.5" width="84.5" height="21" fill="none" stroke="var(--stone)" stroke-width="1"/>
    <text x="77" y="160" text-anchor="middle" font-size="12.5" font-weight="300" fill="var(--navy)">Hair Pomade</text>
    <text x="159" y="160" text-anchor="middle" font-size="12.5" font-weight="300" fill="var(--stone)">Fresh &amp; Clean</text>
    <text x="120" y="188" text-anchor="middle" font-size="9.5" font-weight="300" fill="var(--stone)">NET WT 2 oz (57g)</text>
    <text font-size="9" font-weight="500" fill="var(--stone)"><textPath href="#holdArcNavy" startOffset="50%" text-anchor="middle">Medium Hold – Matte Finish</textPath></text>
  </svg>

  <svg class="lid lid--white" viewBox="0 0 240 240" aria-label="White lid label">
    <defs>
      <path id="holdArcWhite" d="M 10,150 A 92 92 0 0 0 230,150"/>
    </defs>
    <circle cx="120" cy="120" r="113" fill="var(--paper)" stroke="var(--rule-grey)" stroke-width="1"/>
    <circle cx="120" cy="120" r="105" fill="none" stroke="var(--rule-grey)" stroke-width="0.8"/>
    <text x="120" y="104" text-anchor="middle" font-size="48" font-weight="700" fill="var(--navy)" letter-spacing="-1">Brant</text>
    <rect x="37" y="144" width="80" height="22" fill="var(--navy)"/>
    <rect x="117" y="144.5" width="84.5" height="21" fill="none" stroke="var(--navy)" stroke-width="1"/>
    <text x="77" y="160" text-anchor="middle" font-size="12.5" font-weight="300" fill="var(--paper)">Hair Pomade</text>
    <text x="159" y="160" text-anchor="middle" font-size="12.5" font-weight="300" fill="var(--navy)">Fresh &amp; Clean</text>
    <text x="120" y="188" text-anchor="middle" font-size="9.5" font-weight="300" fill="var(--navy)">NET WT 2 oz (57g)</text>
    <text font-size="9" font-weight="500" fill="var(--navy)"><textPath href="#holdArcWhite" startOffset="50%" text-anchor="middle">Medium Hold – Matte Finish</textPath></text>
  </svg>

  <section class="label label--navy">
    <div class="label__maker">
      <p class="label__heading">MANUFACTURED BY:</p>
      <p>Brant Health Products, Millbrook, NC 27514</p>
      <p>Visit us at branthealthproducts.com</p>
    </div>
    <ul class="label__bullets">
      <li>• Naturally derived plant &amp; bee-based ingredients</li>
      <li>• Alcohol Free, Non-Irritating</li>
      <li>• Formulated to minimize scalp irritation</li>
    </ul>
    <div class="label__brand">
      <div class="brand-dot"></div>
      <p class="brand-name">Brant</p>
    </div>
    <p class="label__hold">Medium Hold – Matte Finish</p>
    <p class="label__product">Hair Pomade</p>
    <p class="label__scent">Fresh &amp; Clean</p>
    <p class="label__weight">NET WT 2 oz (57g)</p>
    <div class="label__info">
      <p class="label__heading">DIRECTIONS:</p>
      <p>Melt small amount of pomade between hands before massaging into damp hair (for sleeker look) or dry hair (for more texture). Style as desired. For external use only. Avoid contact with eyes. If irritation occurs, discontinue use.</p>
      <p class="label__heading">INGREDIENTS:</p>
      <p>Butyrospermum Parkii (Shea Butter), Cera Alba (Beeswax), Polyglycerol-3 Beeswax (Cera Bellina), Caprylic/Capric Triglyceride (Fractionated Coconut Oil), Tocopherol (Vitamin E), Fragrance (Parfum)</p>
    </div>
  </section>

  <section class="label label--white">
    <div class="label__maker">
      <p class="label__heading">MANUFACTURED BY:</p>
      <p>Brant Health Products, Millbrook, NC 27514</p>
      <p>Visit us at branthealthproducts.com</p>
    </div>
    <ul class="label__bullets">
      <li>• Naturally derived plant &amp; bee-based ingredients</li>
      <li>• Alcohol Free, Non-Irritating</li>
      <li>• Formulated to minimize scalp irritation</li>
    </ul>
    <div class="label__brand">
      <div class="brand-dot"></div>
      <p class="brand-name">Brant</p>
    </div>
    <p class="label__hold">Medium Hold – Matte Finish</p>
    <p class="label__product">Hair Pomade</p>
    <p class="label__scent">Fresh &amp; Clean</p>
    <p class="label__weight">NET WT 2 oz (57g)</p>
    <div class="label__info">
      <p class="label__heading">DIRECTIONS:</p>
      <p>Melt small amount of pomade between hands before massaging into damp hair (for sleeker look) or dry hair (for more texture). Style as desired. For external use only. Avoid contact with eyes. If irritation occurs, discontinue use.</p>
      <p class="label__heading">INGREDIENTS:</p>
      <p>Butyrospermum Parkii (Shea Butter), Cera Alba (Beeswax), Polyglycerol-3 Beeswax (Cera Bellina), Caprylic/Capric Triglyceride (Fractionated Coconut Oil), Tocopherol (Vitamin E), Fragrance (Parfum)</p>
    </div>
  </section>
</body>
</html>
```